KRV Inc Web Design

WHAT ARE WE DOING?
We are developing a new website look and feel for a new company called KRV Inc. This new look and feel should include colors, design elements, choice of photography and other imagery, fonts, and other user experience elements.

WHAT DO THEY DO?
KRV, Inc, makes tools for researchers who are studying protein-protein interactions. These molecules are the basic tools of biology, and serve as key targets for drug developers and disease researchers. The world of proteins is enormously complex, and companies like KRV provide researchers with critical tools that help them elucidate this world.

WHO ARE WE TALKING TO?
The target audience for this website are professional scientists working in university research or biopharma drug development. They are highly sophisticated consumers looking for key tools that will advance their research.

WHAT DO WE WANT THEM TO DO?
The site is an information resource for the customer exploring the tools that KRV sells and the scientific issues surrounding protein-protein interactions. They should be able to navigate easily to their content of choice, while the whole site should convey a professionalism that enhanced KRV’s credibility.

WHAT DOES THE KRV BRAND STAND FOR?
KRV stands for illumination. Proteins are challenging to study, and KRV exists to help shed light on their workings.

WHAT ARE THE KEY VALUES OF THE KRV BRAND?
Integrity. Innovation. Insight.

WHAT ARE THE EXECUTIONAL MANDITORIES?
The look and feel is completely up for grabs. Nothing is off the table.

WHAT ARE THE DELIVERABLES?
We need new designs for the following templates:
http://cms.thevormelgroup.com/
http://cms.thevormelgroup.com/products-and-services/instruments-3/bench-top-instruments/
http://cms.thevormelgroup.com/category/lab-study/

```html
<!DOCTYPE html>
<html lang="en">
<head>
<meta charset="utf-8">
<title>KRV Inc</title>
<link href="https://fonts.googleapis.com/css2?family=Arimo:wght@400;700&family=PT+Sans:wght@400;700&display=swap" rel="stylesheet">
<style>
:root{
  --teal:#1a9fc4;
  --teal-dark:#0c6f8c;
  --ink:#111;
  --body:#666;
  --nav:#555;
  --orange:#f39322;
  --footer-top:#3b3d40;
  --footer-bottom:#050505;
  --rule:#c9c9c9;
}
*{margin:0;padding:0;box-sizing:border-box}
html,body{width:1200px;height:1114px;overflow:hidden}
body{
  position:relative;
  font-family:Arimo,Arial,sans-serif;
  background:radial-gradient(ellipse 70% 60% at 50% 15%,#f4fbfd 0%,#cfeaf3 45%,#7fc9e0 85%,#5bb9d6 100%);
}
.abs{position:absolute}

/* header */
.brand{left:250px;top:26px;display:flex;align-items:center;gap:10px}
.brand-mark{width:76px;height:76px;border-radius:50%;background:var(--teal)}
.brand-name{font-family:Arimo,Arial,sans-serif;font-weight:700;font-size:38px;line-height:36px;color:var(--ink);letter-spacing:1px}
.social{top:38px;width:16px;height:16px;border-radius:3px;background:#c7d6dc}
.search{left:826px;top:37px;width:124px;height:17px;border-radius:9px;background:#fff;border:1px solid #bbb;overflow:hidden}
.search span{position:absolute;left:9px;top:2px;font-size:9px;color:#333}
.search-btn{position:absolute;right:0;top:0;width:21px;height:17px;background:#111}
.nav{top:86px;right:250px;display:flex;gap:19px;align-items:center;font-size:12px;color:var(--nav)}
.nav .active{background:linear-gradient(#555,#222);color:#fff;padding:2px 10px;border-radius:8px}

/* page */
.page{left:250px;top:117px;width:700px;height:733px;background:#fff;border:1px solid #ddd}
.hero{left:261px;top:126px;width:678px;height:292px;border:1px solid #bbb;
  background:radial-gradient(circle at 40% 30%,#f3c7a0 0%,#c55a3a 22%,#5c1c14 55%,#1f0707 100%)}
.hero-caption{left:0;top:167px;width:359px;height:107px;background:rgba(20,8,6,.82);padding:10px 15px}
.hero-caption h2{font-size:16px;line-height:21px;color:#fff;font-weight:700}
.btn{display:inline-block;background:linear-gradient(#1aa6c9,#0a6e8c);color:#fff;font-size:10px;border-radius:8px;padding:2px 9px;box-shadow:0 1px 2px rgba(0,0,0,.4)}
.hero-caption .btn{margin-top:8px}

h1.welcome{left:261px;top:436px;font-size:19px;font-weight:400;color:var(--ink)}
h1.welcome em{font-style:normal;color:var(--teal)}
.intro{left:264px;top:466px;width:472px;font-size:8.4px;line-height:15.2px;color:var(--body)}
.divider{left:747px;top:442px;height:108px;border-left:1px dotted #bbb}
.newsletter h3{font-size:19px;font-weight:400;color:var(--ink)}
.newsletter{left:761px;top:436px}
.nl-input{left:762px;top:469px;width:121px;height:22px;border:1px solid #ccc;background:#fff}
.nl-send{left:883px;top:469px;width:35px;height:22px;background:var(--orange);color:#fff;font-size:10px;display:flex;align-items:center;justify-content:center}
.contact{left:762px;font-size:8.5px;color:#222;display:flex;gap:5px;align-items:center}

.feature{top:575px;width:215px}
.feature h3{font-size:19px;font-weight:400;color:var(--ink)}
.feature small{display:block;font-size:6.5px;color:#555;margin-top:3px;padding-bottom:6px;border-bottom:1px solid var(--rule)}
.feature-img{margin:12px 0 0 2px;width:211px;height:100px;border:1px solid #ccc}
.feature p{margin:9px 0 0 2px;font-size:8.4px;line-height:15.2px;color:var(--body)}
.feature .btn{margin:10px 0 0 2px;font-size:10px;padding:2px 9px}

/* footer */
.footer{left:250px;top:850px;width:700px;height:195px;background:linear-gradient(var(--footer-top),var(--footer-bottom));color:#fff;font-family:"PT Sans",Arial,sans-serif}
.footer h4{position:absolute;font-size:14px;font-weight:700}
.about{left:18px;top:18px}
.about-text{position:absolute;left:18px;top:44px;width:580px;font-size:9px;line-height:15px}
.col{position:absolute;top:92px}
.col ul{list-style:none;margin-top:11px;font-size:9.5px;line-height:18px}
.col h4{position:static}
.legal{top:1050px;font-family:"PT Sans",Arial,sans-serif;font-size:10px;color:#111}
</style>
</head>
<body>

<header>
  <div class="abs brand">
    <span class="brand-mark"></span>
    <span class="brand-name">KRV<br>INC</span>
  </div>
  <span class="abs social" style="left:783px"></span>
  <span class="abs social" style="left:805px"></span>
  <div class="abs search"><span>search..</span><div class="search-btn"></div></div>
  <nav class="abs nav">
    <span class="active">Company</span>
    <span>Products &amp; Services</span>
    <span>Learning Center</span>
    <span>Events</span>
    <span>KRV News</span>
    <span>Contact Us</span>
  </nav>
</header>

<main>
  <div class="abs page"></div>

  <section class="abs hero" role="img" aria-label="Close-up photo of a glass dropper releasing liquid into a laboratory dish under warm light">
    <div class="abs hero-caption">
      <h2>The Majority of GPCR-based drug discovery programs have failed to yield highly selective compounds.</h2>
      <span class="btn">Learn More</span>
    </div>
  </section>

  <h1 class="abs welcome">Welcome to <em>KRV INC.</em></h1>
  <p class="abs intro">Lorem Ipsum is simply dummy text of the printing and typesetting industry. Lorem Ipsum has been the industry's standard dummy text ever since the 1500s, when an unknown printer took a galley of type and scrambled it to make a type specimen book. It has survived not only five centuries, but also the leap into electronic typesetting, remaining essentially unchanged. It was popularised in the 1960s with the release of Tessaline sheets containing Lorem Ipsum passages, and more recently with desktop publishing software like Quillset PageForge including versions of Lorem Ipsum.</p>

  <div class="abs divider"></div>
  <div class="abs newsletter"><h3>Newsletter</h3></div>
  <div class="abs nl-input"></div>
  <div class="abs nl-send">SEND</div>
  <div class="abs contact" style="top:502px">
    <svg width="7" height="9" viewBox="0 0 7 9"><path d="M1 0h2l-.5 2.5-1 .5c.4 1.5 1.2 2.6 2.3 3.2l.8-.6L7 6.8 6 9C3 8.6.6 5.5 0 1.5z" fill="#111"/></svg>
    Corporate Headquarters 04180-2027
  </div>
  <div class="abs contact" style="top:520px">
    <svg width="7" height="9" viewBox="0 0 7 9"><path d="M1 0h2l-.5 2.5-1 .5c.4 1.5 1.2 2.6 2.3 3.2l.8-.6L7 6.8 6 9C3 8.6.6 5.5 0 1.5z" fill="#111"/></svg>
    KRV South (800) 555-0142
  </div>

  <section class="abs feature" style="left:265px">
    <h3>Innovation</h3>
    <small>dummy text of the printing and typesetting industry.</small>
    <div class="feature-img" role="img" aria-label="Colourful ribbon model of a protein structure" style="background:linear-gradient(90deg,#3c8a1e,#c8b21a 35%,#d12ab8 60%,#5a1a8a)"></div>
    <p>Lorem Ipsum is simply dummy text of the printing and typesetting industry. Lorem Ipsum has been the industry's standard dummy text ever since the 1500s, when an unknown printer took a galley of type and scrambled it to make a type specimen book</p>
    <span class="btn">Learn More</span>
  </section>

  <section class="abs feature" style="left:492px">
    <h3>Automation</h3>
    <small>dummy text of the printing and typesetting industry.</small>
    <div class="feature-img" role="img" aria-label="Gloved hand placing a sample tube into a rack of test tubes" style="background:linear-gradient(90deg,#8ea4b8,#c9d4de 50%,#e9eef2)"></div>
    <p>Lorem Ipsum is simply dummy text of the printing and typesetting industry. Lorem Ipsum has been the industry's standard dummy text ever since the 1500s, when an unknown printer took a galley of type and scrambled it to make a type specimen book</p>
    <span class="btn">Order Today</span>
  </section>

  <section class="abs feature" style="left:721px">
    <h3>Research</h3>
    <small>dummy text of the printing and typesetting industry.</small>
    <div class="feature-img" role="img" aria-label="Scientist in a lab coat and hair net examining a glass beaker" style="background:linear-gradient(90deg,#e6e9ec,#cfd5da 60%,#eef0f2)"></div>
    <p>Lorem Ipsum is simply dummy text of the printing and typesetting industry. Lorem Ipsum has been the industry's standard dummy text ever since the 1500s, when an unknown printer took a galley of type and scrambled it to make a type specimen book</p>
    <span class="btn">The Challenge</span>
  </section>
</main>

<footer class="abs footer">
  <h4 class="about">About us</h4>
  <p class="about-text">Lorem Ipsum is simply dummy text of the printing and typesetting industry. Lorem Ipsum has been the industry's standard dummy text ever since the 1500s, when an unknown printer took a galley of type and scrambled it to make a type specimen book. I</p>
  <div class="col" style="left:28px"><h4>Company</h4><ul><li>Lorem Ipsum</li><li>Lorem Ipsum</li><li>Lorem Ipsum</li></ul></div>
  <div class="col" style="left:157px"><h4>Products &amp; Services</h4><ul><li>Lorem Ipsum</li><li>Lorem Ipsum</li><li>Lorem Ipsum</li></ul></div>
  <div class="col" style="left:329px"><h4>Learning Center</h4><ul><li>Lorem Ipsum</li><li>Lorem Ipsum</li><li>Lorem Ipsum</li></ul></div>
  <div class="col" style="left:488px"><h4>Events</h4><ul><li>Lorem Ipsum</li><li>Lorem Ipsum</li><li>Lorem Ipsum</li></ul></div>
  <div class="col" style="left:596px"><h4>KRV News</h4><ul><li>Lorem Ipsum</li><li>Lorem Ipsum</li><li>Lorem Ipsum</li></ul></div>
</footer>
<p class="abs legal" style="left:250px">© 2013 Demo Site.</p>

</body>
</html>
```